HELMLANE COWORKING Website design and coding

HELMLANE COWORKING

HELMLANE is Port Alder’s first (and currently only) shared business co-working space. We share the same upscale, casual work environment, but we work independently on our own (or our team’s) projects and goals. For only a flat $195 membership fee per month, you have your very own all-inclusive, fun, personal business office environment. Website is written (Word file #12, below); and all pictures etc provided. Port Alder is a beachy, coastal, historic city an hour from Bayridge, Texas USA. Logo (file 11 below) is temporary only.

Target Market(s)

Outside sales people, medical students looking for study hall, Bayridge companies looking for local office, real estate agents, graphic artists, entrepreneurs, etc

Contact Information for Business Card

will discuss --want to combine with current business card with multiple businesses

Logo Text

HELMLANE COWORKING

Coding

Coded - Design and coding required

Number of Pages Required

5+ page

Colors
ec1f27
fbed22

Requirements
Nice to have
• maroon/wine dominant with yellow and red accents, gray base are the colors of the space--website could coordinate--but open to creative ideas/combinations

```html
<!DOCTYPE html>
<html lang="en">
<head>
<meta charset="utf-8">
<title>HELMLANE COWORKING</title>
<link href="https://fonts.googleapis.com/css2?family=Libre+Baskerville:wght@700&family=Oswald:wght@500&family=Poppins:wght@300;400;500;600;700&display=swap" rel="stylesheet">
<style>
:root{
  --wine:#8b0a0f;
  --red:#ec1f27;
  --deep-red:#b30d14;
  --yellow:#fbed22;
  --ink:#333333;
  --muted:#666666;
  --grey:#f3f3f3;
  --footer:#0e0e0e;
  --white:#ffffff;
}
*{box-sizing:border-box;margin:0;padding:0}
html,body{width:1200px;height:4409px;overflow:hidden}
body{position:relative;background:var(--white);font-family:"Poppins",sans-serif;color:var(--ink);font-weight:300}
.abs{position:absolute}
.serif{font-family:"Libre Baskerville",serif;font-weight:700}

/* header */
.brand{left:60px;top:14px;text-align:center;line-height:1}
.brand-name{font-family:"Libre Baskerville",serif;font-weight:700;font-size:28px;color:var(--wine);letter-spacing:1px}
.brand-sub{font-weight:700;font-size:15px;color:#111;letter-spacing:1px;margin-top:4px}
.nav{right:66px;top:36px;display:flex;gap:17px;font-size:10.5px;font-weight:400;color:#444;letter-spacing:.3px}
.nav .active{color:var(--yellow);border-bottom:1px solid var(--yellow);padding-bottom:6px}

/* hero */
.hero-art{left:0;top:0}
.hero-tag{left:221px;top:425px;font-family:"Oswald",sans-serif;font-size:12px;color:var(--wine);letter-spacing:.2px}
.hero-title{left:219px;top:450px;font-size:37px;line-height:46px;color:#222;font-weight:300}
.hero-title strong{font-weight:400}
.dots{left:221px;top:566px;display:flex;align-items:center;gap:8px}
.dot{width:8px;height:8px;border-radius:50%;background:#c8c8c8}
.dot.on{width:13px;height:13px;border:2px solid var(--wine);background:#fff}
.dash{width:22px;height:1px;background:var(--wine)}

/* about */
.about-bg{left:0;top:700px}
.eyebrow{font-size:14px;font-weight:400;color:#222}
.about-eyebrow{left:633px;top:796px}
.about-title{left:633px;top:823px;font-size:31px;line-height:34px;color:var(--wine);letter-spacing:1px}
.about-copy{left:637px;top:906px;width:350px;font-size:11px;line-height:21px;color:var(--muted)}
.about-copy p+p{margin-top:10px}

.btn{display:flex;align-items:center;justify-content:space-between;background:var(--yellow);border-radius:20px;padding-left:20px;height:38px;font-family:"Libre Baskerville",serif;font-weight:700;font-size:13px;color:var(--wine);letter-spacing:.5px}
.btn-arrow{width:38px;height:38px;border-radius:50%;background:var(--deep-red);border:3px solid var(--yellow);display:flex;align-items:center;justify-content:center}

/* amenities */
.center{left:0;width:1200px;text-align:center}
.why{top:1320px}
.amen-title{top:1346px;font-size:30px;color:var(--wine);letter-spacing:1px}
.amen-card{left:281px;top:1414px;width:638px;height:337px;border-radius:4px;overflow:hidden}
.amen-photo{height:260px;background:linear-gradient(180deg,#d9c6a8 0%,#8a6a45 45%,#3b2d22 100%)}
.amen-caption{height:77px;background:#e9dc23;padding:20px 27px;font-size:11.5px;line-height:19px;color:#333}
.amen-list{list-style:none;font-size:11.5px;line-height:19px;color:#333}
.amen-list li{position:absolute;padding-left:24px}
.amen-list li::before{content:"";position:absolute;left:3px;top:4px;width:9px;height:9px;transform:rotate(45deg);background:var(--yellow);box-shadow:inset 0 0 0 2.5px var(--yellow),inset 0 0 0 10px var(--deep-red)}

/* pictures */
.pic-bg{left:0;top:2185px;width:1200px;height:420px}
.pic-title{top:2255px;font-size:30px;color:var(--wine);letter-spacing:1px}
.tile{top:2330px;width:231px;height:226px}
.tile-red{background:rgba(190,12,18,.88);display:flex;align-items:center;justify-content:center;gap:10px}
.ring{width:36px;height:36px;border-radius:50%;background:var(--yellow);display:flex;align-items:center;justify-content:center}
.pager{top:2412px;width:62px;height:62px;border-radius:50%;background:var(--white);display:flex;align-items:center}

/* membership */
.member-title{top:2750px;font-size:30px;color:var(--white);letter-spacing:1px}
.member-copy{left:420px;top:2800px;width:358px;text-align:center;font-size:11.5px;line-height:19px;color:#fbe3e3}
.member-copy p+p{margin-top:8px}
.member-cta{left:420px;top:2953px;width:358px;text-align:center;font-size:13.5px;line-height:22px;color:var(--white);font-weight:400}
.member-cta a{color:var(--yellow);font-family:"Libre Baskerville",serif;font-weight:700;text-decoration:underline}
.member-figure{left:505px;top:3020px;width:265px;height:268px;border-radius:40px;background:radial-gradient(circle at 50% 45%,#e8eef6 0%,#aebfd6 55%,rgba(255,255,255,0) 72%)}

/* philosophy */
.philo-title{top:3373px;font-size:29px;line-height:38px;color:var(--wine);letter-spacing:1px}
.value{top:3482px;width:232px;text-align:center}
.value-icon{width:100px;height:100px;margin:0 auto}
.value h3{font-family:"Libre Baskerville",serif;font-weight:700;font-size:13px;line-height:21px;color:#222;margin-top:34px;letter-spacing:.3px}
.value p{font-size:11px;line-height:20px;color:var(--muted);margin-top:8px}
.more{display:inline-block;margin-top:13px;font-size:11px;font-weight:500;color:var(--wine);text-decoration:underline}
.more::after{content:" »";color:var(--yellow);text-decoration:none}

/* contact */
.contact{left:0;top:3835px;width:1200px;height:329px;background:linear-gradient(115deg,#9a0b10 0%,#c5141b 55%,#8e0a0f 100%)}
.contact-title{left:204px;top:3950px;font-size:30px;color:var(--white);letter-spacing:1px}
.contact-sub{left:204px;top:3994px;width:250px;font-size:12px;line-height:21px;color:#fde5e5}
.field{height:36px;background:var(--white);border-radius:5px;font-size:11px;color:#777;padding:11px 14px}

/* footer */
.footer{left:0;top:4164px;width:1200px;height:245px;background:var(--footer)}
.f-head{top:4220px;font-family:"Libre Baskerville",serif;font-weight:700;font-size:13px;color:var(--deep-red);letter-spacing:.5px}
.f-line{font-size:12px;line-height:20px;color:#cfcfcf;padding-left:30px}
.f-line svg{position:absolute;left:0;top:2px}
.copy{top:4378px;font-size:11px;color:#bbb}
.copy span{color:var(--deep-red)}
.social{top:4369px;width:32px;height:32px;border:1px solid var(--yellow);display:flex;align-items:center;justify-content:center}
.social i{width:12px;height:12px;background:var(--deep-red)}
</style>
</head>
<body>

<!-- HERO -->
<svg class="abs hero-art" width="1200" height="700" viewBox="0 0 1200 700">
  <defs>
    <linearGradient id="barGrad" x1="0" y1="1" x2="1" y2="0">
      <stop offset="0" stop-color="#a80d13"/><stop offset="1" stop-color="#ec1f27"/>
    </linearGradient>
    <linearGradient id="photoGrad" x1="0" y1="0" x2="1" y2="1">
      <stop offset="0" stop-color="#7f7a63"/><stop offset=".5" stop-color="#b9b7b0"/><stop offset="1" stop-color="#e2e2e0"/>
    </linearGradient>
  </defs>
  <polygon points="640,700 1200,250 1200,700" fill="#f1f1f1"/>
  <line x1="238" y1="322" x2="580" y2="-20" stroke="url(#barGrad)" stroke-width="72" stroke-linecap="round"/>
  <rect role="img" aria-label="Photo of a professional woman holding a notebook in the coworking space" x="-280" y="-280" width="560" height="560" rx="70" fill="url(#photoGrad)" transform="translate(798,290) rotate(45)"/>
  <rect x="377" y="397" width="251" height="148" fill="#ffffff" fill-opacity=".82"/>
</svg>

<header>
  <div class="abs brand">
    <div class="brand-name">HELMLANE</div>
    <div class="brand-sub">COWORKING</div>
  </div>
  <nav class="abs nav">
    <span class="active">HOME</span><span>ABOUT</span><span>AMENITIES</span><span>MEMBERSHIP</span><span>PICTURES</span><span>THE HELMLANE PHILOSOPHY</span><span>CONTACT</span>
  </nav>
</header>

<div class="abs hero-tag">FOR ONLY A FLAT $195 MEMBERSHIP FEE PER MONTH</div>
<h1 class="abs hero-title">World's 1st Private<br><strong>Coworking Space</strong></h1>
<div class="abs dots"><span class="dot on"></span><span class="dash"></span><span class="dot"></span><span class="dot"></span><span class="dot"></span><span class="dot"></span></div>

<!-- ABOUT -->
<svg class="abs about-bg" width="1200" height="546" viewBox="0 0 1200 546">
  <defs>
    <linearGradient id="aboutImg" x1="0" y1="0" x2="1" y2="1">
      <stop offset="0" stop-color="#d9dde0"/><stop offset=".55" stop-color="#8a8d92"/><stop offset="1" stop-color="#2a2a2c"/>
    </linearGradient>
  </defs>
  <polygon points="0,420 1200,80 1200,546 0,546" fill="#f5f5f5"/>
  <rect role="img" aria-label="Photo of the lounge with leather sofas and lockers" x="-133" y="-133" width="266" height="266" rx="40" fill="url(#aboutImg)" transform="translate(353,279) rotate(45)"/>
  <rect x="-36" y="-36" width="72" height="72" rx="12" fill="#e9dc23" fill-opacity=".92" transform="translate(421,406) rotate(45)"/>
</svg>

<section>
  <div class="abs eyebrow about-eyebrow">ABOUT</div>
  <h2 class="abs serif about-title">HELMLANE<br>COWORKING</h2>
  <div class="abs about-copy">
    <p>HELMLANE is Port Alder's first (and currently only) shared business co-working space. We share the same upscale, casual work environment, but we work independently on our own (or our team's) projects and goals.</p>
    <p>For only a flat $195 membership fee per month, you have your very own all-inclusive, fun, personal business office environment.</p>
  </div>
  <div class="abs btn" style="left:639px;top:1084px;width:171px">KNOW MORE
    <span class="btn-arrow"><svg width="14" height="12" viewBox="0 0 14 12"><path d="M2 1l5 5-5 5M7 1l5 5-5 5" fill="none" stroke="#fff" stroke-width="1.8"/></svg></span>
  </div>
</section>

<!-- AMENITIES -->
<section>
  <div class="abs center eyebrow why">WHY US ?</div>
  <h2 class="abs center serif amen-title">AMENITIES</h2>
  <div class="abs amen-card">
    <div class="amen-photo" role="img" aria-label="Photo of the open work area with desks, pendant lamps and kitchen"></div>
    <div class="amen-caption">HELMLANE is the first Port Alder co-working space, and offers all of the following features, all included in your monthly $195 membership fee:</div>
  </div>
  <ul class="amen-list">
    <li style="left:291px;top:1792px;width:270px">Open office or a private cubicle for your daily use.</li>
    <li style="left:291px;top:1845px;width:270px">Free Wifi</li>
    <li style="left:291px;top:1876px;width:270px">Comfortable open casual spaces or private office cubicles – at your option</li>
    <li style="left:291px;top:1926px;width:270px">Keyless, digital door entry</li>
    <li style="left:291px;top:1956px;width:270px">Great location – a block from Port Alder's Market Street area of coffee bars, restaurants, bars, art galleries, and the Old Harbor Theatre</li>
    <li style="left:618px;top:1792px;width:290px">Communal coffee bar and kitchen, with FREE coffee.</li>
    <li style="left:618px;top:1845px;width:290px">24 hour access.</li>
    <li style="left:618px;top:1876px;width:290px">Great opportunity for networking or mentoring.</li>
    <li style="left:618px;top:1926px;width:290px">Mail service.</li>
    <li style="left:618px;top:1956px;width:290px">Weekly FREE happy hour with complimentary cocktails, beer and wine. A great opportunity to make new friends and business contacts.</li>
  </ul>
  <div class="abs btn" style="left:514px;top:2070px;width:171px">EXPLORE ALL
    <span class="btn-arrow"><svg width="14" height="12" viewBox="0 0 14 12"><path d="M2 1l5 5-5 5M7 1l5 5-5 5" fill="none" stroke="#fff" stroke-width="1.8"/></svg></span>
  </div>
</section>

<!-- PICTURES -->
<section>
  <div class="abs pic-bg" style="background:linear-gradient(180deg,#f4f4f4 0%,#f4f4f4 80%,#ffffff 100%)"></div>
  <h2 class="abs center serif pic-title">PICTURE</h2>
  <div class="abs tile" style="left:0;background:linear-gradient(160deg,#e6e4de,#7d7a72 60%,#2e2c29)" role="img" aria-label="Photo of the lounge area"></div>
  <div class="abs tile tile-red" style="left:241px" role="img" aria-label="Photo of the workspace with gallery hover overlay">
    <span class="ring"><svg width="16" height="16" viewBox="0 0 16 16"><path d="M10 4l-5 5a2 2 0 003 3l6-6a3 3 0 00-4-4L4 8" fill="none" stroke="#8b0a0f" stroke-width="1.6"/></svg></span>
    <span class="ring"><svg width="16" height="16" viewBox="0 0 16 16"><circle cx="7" cy="7" r="5" fill="none" stroke="#8b0a0f" stroke-width="1.6"/><path d="M11 11l4 4M5 7h4M7 5v4" stroke="#8b0a0f" stroke-width="1.6"/></svg></span>
  </div>
  <div class="abs tile" style="left:484px;background:linear-gradient(180deg,#4a3a2c,#8c7050 55%,#c89a70)" role="img" aria-label="Photo of the kitchen with a potted plant"></div>
  <div class="abs tile" style="left:727px;background:linear-gradient(180deg,#d8d4c6,#8a826d 55%,#3c3a36)" role="img" aria-label="Photo of the seating area"></div>
  <div class="abs tile" style="left:969px;width:231px;background:linear-gradient(90deg,#3b2b28,#6b5146 50%,#d9d6d0)" role="img" aria-label="Photo of the locker wall"></div>
  <div class="abs pager" style="left:-31px;justify-content:flex-end;padding-right:10px"><svg width="12" height="20" viewBox="0 0 12 20"><path d="M10 2L2 10l8 8" fill="none" stroke="#8b0a0f" stroke-width="2.4"/></svg></div>
  <div class="abs pager" style="left:1169px;padding-left:10px"><svg width="12" height="20" viewBox="0 0 12 20"><path d="M2 2l8 8-8 8" fill="none" stroke="#c9a400" stroke-width="2.4"/></svg></div>
</section>

<!-- MEMBERSHIP -->
<svg class="abs" style="left:0;top:2560px" width="1200" height="800" viewBox="0 0 1200 800">
  <defs>
    <linearGradient id="memGrad" x1="0" y1="0" x2="0" y2="1">
      <stop offset="0" stop-color="#ec1f27"/><stop offset="1" stop-color="#8e0a0f"/>
    </linearGradient>
  </defs>
  <polygon points="860,540 1200,280 1200,660" fill="#f3f3f3"/>
  <rect x="-215" y="-215" width="430" height="430" rx="60" fill="#fbed22" transform="translate(592,372) rotate(45)"/>
  <rect x="-213" y="-213" width="426" height="426" rx="58" fill="url(#memGrad)" transform="translate(600,366) rotate(45)"/>
</svg>
<section>
  <h2 class="abs center serif member-title">MEMBERSHIP</h2>
  <div class="abs member-copy">
    <p>For only $195 a month, charged to your credit card, you get the all-inclusive amenities listed above, for one flat fee. The only "extras" are for copies, on a per-copy basis.</p>
    <p>WiFi, coffee, use of the conference room, office use, use of the kitchen and all the other features listed under "AMENITIES" above, are INCLUDED at no additional cost.</p>
  </div>
  <div class="abs member-cta">Get A FREE Day, To Try Us Out By Emailing<br>Us At The <a>Link Here</a></div>
  <div class="abs member-figure" role="img" aria-label="Illustration of a man sitting cross-legged using a tablet"></div>
</section>

<!-- PHILOSOPHY -->
<section>
  <h2 class="abs center serif philo-title">THE HELMLANE<br>PHILOSOPHY</h2>

  <div class="abs value" style="left:113px">
    <svg class="value-icon" viewBox="0 0 100 100"><rect x="-33" y="-33" width="66" height="66" rx="10" fill="#fbed22" transform="translate(50,50) rotate(45)"/><circle cx="50" cy="50" r="12" fill="none" stroke="#8b0a0f" stroke-width="3"/></svg>
    <h3>WORK OUTSIDE THE<br>HOME</h3>
    <p>Free yourself for the burdens of house or school, and work in an environment that MOTIVATES you instead...</p>
    <span class="more">MORE</span>
  </div>
  <div class="abs value" style="left:360px">
    <svg class="value-icon" viewBox="0 0 100 100"><rect x="-33" y="-33" width="66" height="66" rx="10" fill="#b30d14" transform="translate(50,50) rotate(45)"/><circle cx="50" cy="50" r="12" fill="none" stroke="#fbed22" stroke-width="3"/></svg>
    <h3>OUTPACE THE<br>COMPETITION</h3>
    <p>Because of the flexibility, prestigious location, opportunities to meet and network with active....</p>
    <span class="more">MORE</span>
  </div>
  <div class="abs value" style="left:606px">
    <svg class="value-icon" viewBox="0 0 100 100"><rect x="-33" y="-33" width="66" height="66" rx="10" fill="#fbed22" transform="translate(50,50) rotate(45)"/><circle cx="50" cy="50" r="12" fill="none" stroke="#8b0a0f" stroke-width="3"/></svg>
    <h3>WORK IT OUT WITH YOUR<br>COWORKERS.</h3>
    <p>HELMLANE is a community if you are making a pot of coffee ask and make enough for everyone...</p>
    <span class="more">MORE</span>
  </div>
  <div class="abs value" style="left:853px">
    <svg class="value-icon" viewBox="0 0 100 100"><rect x="-33" y="-33" width="66" height="66" rx="10" fill="#fbed22" transform="translate(50,50) rotate(45)"/><circle cx="50" cy="50" r="12" fill="none" stroke="#8b0a0f" stroke-width="3"/></svg>
    <h3>WORK OUT THE PATH<br>TO YOUR SUCCESS</h3>
    <p>As your business grows, there are other beautiful, "dedicated desk" private executive...</p>
    <span class="more">MORE</span>
  </div>
</section>

<!-- CONTACT -->
<section>
  <div class="abs contact" role="img" aria-label="Red-tinted photo of the coworking interior"></div>
  <h2 class="abs serif contact-title">CONTACT US</h2>
  <p class="abs contact-sub">Need an have any Question for contact us Today !</p>
  <div class="abs field" style="left:596px;top:3907px;width:239px">Name *</div>
  <div class="abs field" style="left:844px;top:3907px;width:240px">Email *</div>
  <div class="abs field" style="left:596px;top:3951px;width:239px">Phone *</div>
  <div class="abs field" style="left:844px;top:3951px;width:240px;height:81px">Message *</div>
  <div class="abs field" style="left:596px;top:3996px;width:239px">Your Question*</div>
  <div class="abs btn" style="left:596px;top:4044px;width:142px">SEND US
    <span class="btn-arrow"><svg width="14" height="12" viewBox="0 0 14 12"><path d="M2 1l5 5-5 5M7 1l5 5-5 5" fill="none" stroke="#fff" stroke-width="1.8"/></svg></span>
  </div>
</section>

<!-- FOOTER -->
<footer>
  <div class="abs footer"></div>
  <div class="abs brand" style="top:4208px">
    <div class="brand-name" style="color:var(--deep-red)">HELMLANE</div>
    <div class="brand-sub" style="color:#fff">COWORKING</div>
  </div>
  <div class="abs f-line" style="left:60px;top:4272px"><svg width="18" height="14" viewBox="0 0 18 14"><rect x="1" y="1" width="16" height="12" fill="none" stroke="#fbed22" stroke-width="1.5"/><path d="M1 1l8 7 8-7" fill="none" stroke="#fbed22" stroke-width="1.5"/></svg>hello@helmlanecowork.com</div>
  <div class="abs f-line" style="left:60px;top:4302px"><svg width="16" height="16" viewBox="0 0 16 16"><path d="M3 1l3 1 1 4-2 1a9 9 0 004 4l1-2 4 1 1 3-2 2C6 15 1 10 1 3z" fill="#fbed22"/></svg>713-555-0148</div>

  <div class="abs f-head" style="left:337px">PHYSICAL LOCATION</div>
  <div class="abs f-line" style="left:337px;top:4255px;width:200px"><svg width="16" height="18" viewBox="0 0 16 18"><path d="M8 17s-6-6-6-10a6 6 0 0112 0c0 4-6 10-6 10z" fill="none" stroke="#fbed22" stroke-width="1.6"/><circle cx="8" cy="7" r="2" fill="#fbed22"/></svg>Helmlane Coworking 418 Harbor Ave, Suite 101 Port Alder, TX 77591</div>

  <div class="abs f-head" style="left:613px">OWNER</div>
  <div class="abs f-line" style="left:613px;top:4255px;width:230px"><svg width="18" height="14" viewBox="0 0 18 14"><rect x="1" y="1" width="16" height="12" fill="none" stroke="#fbed22" stroke-width="1.5"/><path d="M1 1l8 7 8-7" fill="none" stroke="#fbed22" stroke-width="1.5"/></svg>Birchfield Holdings<br>dana@birchfieldpc.com</div>
  <div class="abs f-line" style="left:613px;top:4302px"><svg width="16" height="16" viewBox="0 0 16 16"><path d="M3 1l3 1 1 4-2 1a9 9 0 004 4l1-2 4 1 1 3-2 2C6 15 1 10 1 3z" fill="#fbed22"/></svg>713-555-0148</div>

  <div class="abs f-head" style="left:889px">MANAGEMENT MAIL</div>
  <div class="abs f-line" style="left:889px;top:4255px;width:200px"><svg width="16" height="18" viewBox="0 0 16 18"><path d="M8 17s-6-6-6-10a6 6 0 0112 0c0 4-6 10-6 10z" fill="none" stroke="#fbed22" stroke-width="1.6"/><circle cx="8" cy="7" r="2" fill="#fbed22"/></svg>Birchfield Holdings<br>225 Bayview St., Suite 200 Bayridge, TX 77012</div>

  <div class="abs center copy">©<span>HELMLANE</span> -2020 All rights reserved</div>
  <div class="abs social" style="left:1039px"><i></i></div>
  <div class="abs social" style="left:1074px"><i></i></div>
  <div class="abs social" style="left:1109px"><i></i></div>
</footer>

</body>
</html>
```